female stress management consultant, doctor, Health & Well-being coach needs a wordpress theme

I am a Stress management consultant, General Practitioner and Health and Well-Being coach who is targeting mainly surgeries/hospitals and corporate business.
I have my own URL drhelgabrunsvik.com and the hosting.
I need a WordPress Website that is easy to maintain and edit to regularly change the content (copy/pictures/action buttons/banners).
I want my website to look professional and elegant for corporate businesses and managers to feel they can trust me and my expertise. At the same time, the website should have a warm and welcoming feel to it. It should feel uplifting and very positive.
I am open to colour suggestions, but please incorporate the following two colours: #F18877 and #D2BB7A. For fonts I prefer grey over black (like #777777).
The website needs to create an impression of "know like and trust".
The website should have a sign-up button for a newsletter, multiple contact buttons over the home page - to write an email to me, contact details top and bottom and the possibility to have a video on the home page top instead of a picture (Best would be that I can change from picture to video to picture in the future without needing a designer). A video that can run in the background with text laid over. A bit like on this website from Tessa Vanrijn: https://www.tessavanrijn.com.
I need 5 pages: Home, About, Services, Contact, free resources. I do NOT need an e-commerce or booking facility as I will neither sell nor let people book through my website. I don't need a blog either.
All the pages need to have a link to my other website (brightpathdaily.co.uk) and it needs to state that the linked website (brightpathdaily) is my website with a blog and for private customers.
Please use the photos I attached if possible. Me with the dogs for the "about" section.

Websites I like: https://www.olgabkr.com, tessavanrijn.com, https://ruthpembly.com (this site is too dark for my liking, but the layout has a simple navigation layout, the important buttons are right up at the side (WorkLattice/social media/CTA), is minimalistic - hence easy to find the important bits).

Target Market(s)

surgeries/doctor offices, hospitals, corporate business

Industry/Entity Type

Health and well-being

Coding

Coded - Design and coding required

Number of Pages Required

5+ page

Font styles to use
Sans Serif

Requirements
Must have
• see project description
Nice to have
• see project description

```html
<!DOCTYPE html>
<html lang="en">
<head>
<meta charset="utf-8">
<title>Dr. Helga Brunsvik – Health &amp; Well-Being</title>
<link href="https://fonts.googleapis.com/css2?family=Crimson+Pro:ital,wght@0,400;0,600;1,400;1,600;1,700&family=Roboto:wght@300;400;500;700&display=swap" rel="stylesheet">
<style>
:root{
  --coral:#F18877;
  --gold:#D2BB7A;
  --ink:#1e1e1e;
  --grey:#777777;
  --mint:#eef5df;
  --mint-deep:#e2eecb;
  --white:#ffffff;
  --bar:#9a9a9a;
}
*{margin:0;padding:0;box-sizing:border-box}
html,body{width:1200px;height:3645px;overflow:hidden}
body{position:relative;background:var(--white);font-family:'Roboto',sans-serif;color:var(--grey)}
.abs{position:absolute}
.serif{font-family:'Crimson Pro',serif;font-style:italic}
.coral{color:var(--coral)}
.label{font-family:'Roboto',sans-serif;font-weight:700;font-size:8px;letter-spacing:1px;color:var(--ink);text-transform:uppercase}
.btn-solid{position:absolute;background:var(--coral);color:var(--white);font-size:10px;font-weight:700;letter-spacing:.4px;display:flex;align-items:center;justify-content:center;text-transform:uppercase}
.btn-line{position:absolute;border:2px solid var(--coral);color:var(--coral);font-size:11px;display:flex;align-items:center;justify-content:center;background:var(--white)}
.photo{position:absolute}

/* header & hero */
.hero{position:absolute;left:0;top:0;width:1200px;height:552px;background:radial-gradient(circle at 30% 40%,#f9fcef 0%,#eaf5d6 55%,#dcefc3 100%)}
.hero-wave{position:absolute;left:0;top:0}
.brand{position:absolute;display:flex;align-items:center;gap:8px}
.brand-dot{width:22px;height:22px;border-radius:50%;background:var(--coral)}
.brand-name{font-family:'Crimson Pro',serif;font-size:22px;color:var(--coral);line-height:1}
.brand-tag{font-family:'Crimson Pro',serif;font-size:11px;color:var(--coral);line-height:1.2}
.nav{position:absolute;left:417px;top:21px;display:flex;font-size:10px;font-weight:500;color:var(--ink)}
.nav a{position:absolute;white-space:nowrap;text-decoration:none;color:inherit}
.nav a.active{color:var(--coral)}
.social-top{position:absolute;top:15px;display:flex}
.social-top span,.social-foot span{position:absolute;border:1.5px solid #555;border-radius:50%}
.hero-title{left:215px;top:148px;font-family:'Crimson Pro',serif;font-style:italic;font-weight:700;font-size:50px;line-height:50px;color:var(--ink);letter-spacing:1px}
.hero-text{left:215px;top:320px;width:320px;font-size:11.5px;line-height:19px;color:#333}

/* about */
.about-pattern{left:215px;top:698px;width:301px;height:342px;background:var(--mint)}
.about-text{left:614px;top:736px;width:330px;font-size:13px;line-height:20px;color:var(--grey);font-weight:300}
.about-head{left:614px;top:640px;font-family:'Crimson Pro',serif;font-style:italic;font-size:40px;line-height:44px;color:var(--ink)}

/* services */
.services{left:0;top:1090px;width:1200px;height:439px;background:var(--mint)}
.h-section{position:absolute;left:0;width:1200px;text-align:center;font-family:'Crimson Pro',serif;font-style:italic;color:var(--ink)}
.svc{position:absolute;top:1231px;width:240px;text-align:center}
.svc-icon{width:80px;height:80px;border-radius:50%;background:var(--white);margin:0 auto;display:flex;align-items:center;justify-content:center}
.svc-title{margin-top:16px;font-family:'Crimson Pro',serif;font-style:italic;font-size:22px;line-height:22px;color:var(--coral)}
.svc-text{margin-top:14px;font-size:11px;line-height:19px;color:#444}
.svc-more{margin-top:12px;font-size:11px;color:var(--coral)}

/* help banner */
.help{left:0;top:1529px;width:1200px;height:244px;background:linear-gradient(90deg,#fdfef8 0%,#f4f9e8 60%,#edf5dc 100%)}

/* video */
.video{left:333px;top:1909px;width:533px;height:300px;background:linear-gradient(135deg,#cfcfcf,#8d8d8d 55%,#5c5c5c)}

/* resources */
.resources{left:0;top:2257px;width:1200px;height:531px;background:var(--mint)}
.card{position:absolute;top:2393px;width:249px;height:346px;background:var(--white)}
.card-img{width:249px;height:153px}
.card-title{margin:17px 0 0 19px;font-family:'Crimson Pro',serif;font-style:italic;font-size:17px;color:var(--ink)}
.card-text{margin:6px 19px 0;font-size:9.5px;line-height:15.5px;color:var(--grey)}
.card .btn-line{left:19px;top:290px;width:114px;height:32px;font-size:10px;position:absolute}

/* testimonials */
.quote{left:270px;top:2934px;width:660px;text-align:center;font-style:italic;font-size:12.5px;line-height:20px;color:var(--grey);font-weight:300}
.dots{left:572px;top:3124px;display:flex;gap:6px}
.dots span{width:9px;height:9px;background:#aaa}
.dots span:first-child{background:var(--coral)}

/* cta */
.cta{left:0;top:3184px;width:1200px;height:226px;background:var(--mint-deep)}

/* footer */
.foot-links{position:absolute;font-size:10.5px;color:#333;line-height:22.6px}
.foot-about{left:214px;top:3503px;width:220px;font-style:italic;font-size:12px;line-height:17.5px;color:#333}
.social-foot span{border-color:#888}
.bottom-bar{left:0;top:3617px;width:1200px;height:28px;background:var(--bar);color:var(--white);font-size:8.5px;display:flex;align-items:center;justify-content:center}
</style>
</head>
<body>

<!-- Header & hero -->
<section class="hero">
  <svg class="hero-wave" width="1200" height="552" viewBox="0 0 1200 552" aria-hidden="true">
    <path d="M560 552 C760 470 930 420 1200 300 L1200 552 Z" fill="#cfe6a8" opacity=".55"/>
    <path d="M640 552 C820 500 980 450 1200 380 L1200 552 Z" fill="#bfdd8e" opacity=".55"/>
    <circle cx="300" cy="420" r="90" fill="#ffffff" opacity=".25"/>
    <circle cx="860" cy="170" r="70" fill="#ffffff" opacity=".3"/>
  </svg>
  <div class="photo" role="img" aria-label="Photo of a smiling senior woman jogging with headphones" style="left:722px;top:57px;width:212px;height:495px;border-radius:100px 100px 0 0;background:linear-gradient(180deg,#e8e8e8 0%,#f1f1f1 45%,#ece6b0 85%,#e9e1a0 100%)"></div>
</section>

<div class="brand" style="left:125px;top:12px">
  <span class="brand-dot"></span>
  <div><div class="brand-name">Dr. Helgabrunsvik</div><div class="brand-tag" style="color:#333">Create a life you love living</div></div>
</div>
<nav class="nav">
  <a class="active" style="left:0">HOME</a>
  <a style="left:57px">ABOUT</a>
  <a style="left:119px">SERVICES</a>
  <a style="left:197px">FREE RESOURCES</a>
  <a style="left:316px">CONTACT</a>
</nav>
<div class="social-top" aria-label="Social links">
  <span style="left:947px;width:24px;height:24px"></span>
  <span style="left:983px;width:24px;height:24px"></span>
  <span style="left:1017px;width:24px;height:24px"></span>
  <span style="left:1051px;width:24px;height:24px"></span>
</div>

<h1 class="abs hero-title">Live a Healthy<br>&amp; Best Life With<br>Full of Joy!</h1>
<p class="abs hero-text">I am a Stress management consultant, General Practitioner and Health and Well-Being coach who is targeting mainly surgeries/hospitals and corporate business.</p>
<a class="btn-solid" style="left:215px;top:402px;width:145px;height:28px">Get a free consultant</a>

<!-- About -->
<div class="abs about-pattern" role="img" aria-label="Faint line pattern of wellness motifs"></div>
<div class="photo" role="img" aria-label="Portrait of Dr. Helga Brunsvik smiling outdoors" style="left:282px;top:601px;width:288px;height:380px;background:linear-gradient(180deg,#8fb36a 0%,#c9b08a 45%,#6f88b8 100%)"></div>
<div class="abs label" style="left:614px;top:616px;font-size:7.5px">Hello !</div>
<h2 class="abs about-head">I'm <span class="coral">Doctor<br>Helgabrunsvik.</span></h2>
<p class="abs about-text">With over 30 years of being a doctor, I've met countless people facing ongoing health issues and struggles that couldn't be solved solely through conventional medicine. That's why it's so important to embrace a holistic approach in our quest for balance, shifting from discomfort to vitality and contentment.</p>
<div class="abs" role="img" aria-label="Handwritten signature" style="left:614px;top:878px;width:80px;height:34px;background:linear-gradient(90deg,#e6e6e6,#cfcfcf)"></div>
<a class="btn-line" style="left:614px;top:942px;width:114px;height:33px">Read More</a>

<!-- Services -->
<section class="abs services"></section>
<div class="abs label" style="left:0;top:1139px;width:1200px;text-align:center;font-size:7.5px">With over 30 years of being a doctor</div>
<h2 class="h-section" style="top:1160px;font-size:40px">This is <span class="coral">What I Do?</span></h2>

<div class="svc" style="left:218px">
  <div class="svc-icon"><svg width="40" height="46" viewBox="0 0 40 46" aria-hidden="true"><circle cx="20" cy="12" r="9" fill="#222"/><path d="M4 46 C4 30 10 24 20 24 C30 24 36 30 36 46 Z" fill="#222"/></svg></div>
  <div class="svc-title">Stress Management<br>Consultant</div>
  <p class="svc-text">I am Stress Management Consultant. If you're feeling stuck, uncertain, or struggling with your health or well-being, one-on-one coaching can provide the guidance and....</p>
  <div class="svc-more">[ Read more... ]</div>
</div>
<div class="svc" style="left:481px">
  <div class="svc-icon"><svg width="42" height="38" viewBox="0 0 42 38" aria-hidden="true"><rect x="14" y="2" width="14" height="8" rx="2" fill="none" stroke="#222" stroke-width="3"/><rect x="2" y="9" width="38" height="27" rx="4" fill="#222"/><path d="M21 15 v14 M14 22 h14" stroke="#fff" stroke-width="4"/></svg></div>
  <div class="svc-title">General<br>Practitioner</div>
  <p class="svc-text">The Medical Doctor and General Practitioner, certified Health and Well-being Coach hold a doctorate degree in virology (PhD); I'm a Meditation teacher, Intentional Creativity....</p>
  <div class="svc-more">[ Read more... ]</div>
</div>
<div class="svc" style="left:743px">
  <div class="svc-icon"><svg width="44" height="40" viewBox="0 0 44 40" aria-hidden="true"><circle cx="22" cy="7" r="6" fill="#222"/><path d="M22 14 L22 28 M22 16 L10 26 M22 16 L34 26 M4 36 Q22 26 40 36" stroke="#222" stroke-width="4" fill="none" stroke-linecap="round"/></svg></div>
  <div class="svc-title">Health and<br>Well-Being coach</div>
  <p class="svc-text">I'm a Meditation teacher, Intentional Creativity Coach and Teacher, artist, friend, mum, and a humble human being who has a wealth of knowledge on how to lead a happy and....</p>
  <div class="svc-more">[ Read more... ]</div>
</div>

<!-- Help banner -->
<section class="abs help"></section>
<div class="abs label coral" style="left:214px;top:1597px;font-size:7.5px;color:var(--coral)">Create a life you love living</div>
<h2 class="abs serif" style="left:212px;top:1614px;font-size:36px;color:var(--ink)">I Help You Live Your Best Life</h2>
<a class="btn-solid" style="left:214px;top:1675px;width:143px;height:28px">Get a free consultant</a>
<div class="photo" role="img" aria-label="Portrait of Dr. Helga Brunsvik in a striped top" style="left:785px;top:1543px;width:201px;height:230px;background:linear-gradient(180deg,#f5f3ea 0%,#d8b998 40%,#7590bd 100%)"></div>

<!-- Video -->
<h2 class="h-section" style="top:1812px;font-size:36px;line-height:38px">It's never too late<br><span class="coral">Virtual Summit 2000</span></h2>
<div class="abs video" role="img" aria-label="Video still of a group yoga class on mats"></div>
<svg class="abs" style="left:574px;top:2034px" width="52" height="52" viewBox="0 0 52 52" aria-hidden="true"><circle cx="26" cy="26" r="26" fill="#ffffff" opacity=".85"/><path d="M20 15 L38 26 L20 37 Z" fill="var(--coral)"/></svg>

<!-- Free resources -->
<section class="abs resources"></section>
<div class="abs label" style="left:0;top:2307px;width:1200px;text-align:center;font-size:7.5px">Our free resources</div>
<h2 class="h-section" style="top:2322px;font-size:40px">that help you live your best life</h2>

<article class="card" style="left:212px">
  <div class="card-img" role="img" aria-label="Photo of a fresh salad plate and glass of wine" style="background:linear-gradient(135deg,#7c93d6,#dfe3ea 60%,#f4f4f4)"></div>
  <h3 class="card-title">Eat Well</h3>
  <p class="card-text">I've met countless people facing ongoing health issues and struggles that couldn't be solved solely through conventional medicine. That's why it's so important to embrace a holistic approach in our quest for balance..</p>
  <a class="btn-line">Get Free Resources</a>
</article>
<article class="card" style="left:475px">
  <div class="card-img" role="img" aria-label="Photo of a joyful woman stretching in a garden" style="background:linear-gradient(135deg,#4f7a2e,#8cab5f 50%,#7d8fc9)"></div>
  <h3 class="card-title">Live Healthy</h3>
  <p class="card-text">The secret to living a joyful, vibrant life lies in nurturing every aspect of yourself, not just your physical body. Surprisingly, it's easier as you might think to harmonize your body, mind, and spirit and experience optimal well-being...</p>
  <a class="btn-line">Get Free Resources</a>
</article>
<article class="card" style="left:737px">
  <div class="card-img" role="img" aria-label="Close-up portrait of a smiling woman" style="background:linear-gradient(135deg,#7a8a56,#d9b89a 55%,#b58f6c)"></div>
  <h3 class="card-title">It's Been So Easy</h3>
  <p class="card-text">They provide knowledge, support, and motivation for positive change. Engaging in these discussions connects you to a community, empowers you with insights, and promotes self-awareness. Get ready for</p>
  <a class="btn-line">Get Free Resources</a>
</article>

<!-- Testimonials -->
<h2 class="h-section" style="top:2838px;font-size:40px">Testimonials</h2>
<h3 class="h-section" style="top:2905px;font-size:18px">Working with Dr Helga helped me to appreciate myself more.</h3>
<p class="abs quote">The workshop has allowed me to appreciate myself more. For what I am. The quality of delivery is what made the experience. Dr Helga's understanding of the guided meditations helped enormously. Being in an exclusive, supportive and safe environment allowed me to get in touch with elements of myself that I was shy of. I'd love more people to be able to access this and to experience this quality of experience.</p>
<div class="photo" role="img" aria-label="Small portrait of the client" style="left:535px;top:3038px;width:52px;height:55px;background:linear-gradient(180deg,#e9e9e9,#9fb0cf)"></div>
<div class="abs coral" style="left:600px;top:3050px;font-size:15px">Lorna P.</div>
<div class="abs" style="left:600px;top:3070px;font-size:11px;color:#555">Private Client</div>
<div class="abs dots"><span></span><span></span><span></span><span></span></div>

<!-- CTA -->
<section class="abs cta"></section>
<h2 class="h-section" style="top:3223px;font-size:36px;line-height:40px">Discover Simple Steps to Restore Your Happiness<br>and Health Today!</h2>
<a class="btn-line" style="left:494px;top:3329px;width:211px;height:30px;border:none;font-size:10px">GET A FREE CONSULTANT TODAY!</a>

<!-- Footer -->
<div class="brand" style="left:214px;top:3443px">
  <span class="brand-dot"></span>
  <div><div class="brand-name">Helgabrunsvik</div><div class="brand-tag">Create a life you love living</div></div>
</div>
<p class="abs foot-about">The time that you invest in yourself, your health and your happiness will be the best investment you can make. You can't buy happiness, but you can create it.</p>
<div class="foot-links" style="left:468px;top:3441px">Home<br>About<br>Services<br>Coaching<br>Free Resources<br>Free Talk Health</div>
<div class="foot-links" style="left:597px;top:3441px">Privacy Policy<br>Disclaimer<br>Health &nbsp;Advice<br>Virtual Summit<br>News &amp; Blog<br>Contact</div>
<h3 class="abs serif" style="left:740px;top:3443px;font-size:20px;line-height:24px;color:var(--ink);font-weight:400">Join our newsletter to get<br>the latest news and tips.</h3>
<div class="abs" style="left:739px;top:3504px;width:167px;height:29px;background:#8f8f8f;color:#eee;font-size:10px;display:flex;align-items:center;padding-left:13px">Your Email Address</div>
<a class="btn-solid" style="left:906px;top:3504px;width:80px;height:29px;font-size:11px;text-transform:none;font-weight:500">Join Now</a>
<div class="social-foot">
  <span style="left:741px;top:3548px;width:22px;height:22px"></span>
  <span style="left:779px;top:3548px;width:22px;height:22px"></span>
  <span style="left:818px;top:3548px;width:22px;height:22px"></span>
  <span style="left:858px;top:3548px;width:22px;height:22px"></span>
</div>
<div class="abs bottom-bar">© 2023 Dr. Helga Brunsvik. All rights reserved. &nbsp;|&nbsp; Consultant, Coach and General Practitioner</div>

</body>
</html>
```